MOSSGATE SPIRITWORKS WEBSITE

MOSSGATE SPIRITWORKS WHOLESALES ALCOHOL (WHISKY VODKA AND HELPS CREATES BOTTLING/BRANDING FOR PEOPLE WANTING LAUNCH THERE OWN BRANDS OF ALCOHOL

Colors

Designer to choose colors to be used in the design.

```html
<!DOCTYPE html>
<html lang="en">
<head>
<meta charset="utf-8">
<title>Mossgate Spiritworks — Wholesale</title>
<link href="https://fonts.googleapis.com/css2?family=Crimson+Text:wght@400;600&display=swap" rel="stylesheet">
<style>
:root{
  --ink:#0e0c0c;
  --band:#221f1f;
  --band-soft:#2a2525;
  --gold:#c9a45c;
  --rose:#b46b75;
  --white:#ffffff;
  --whisky:#fdcba5;
  --whisky-deep:#7a4a38;
  --vodka:#eaf8ff;
  --vodka-deep:#8fb7d8;
  --rum:#5c4037;
  --rum-deep:#1c1412;
  --gin:#c9fdc7;
  --gin-deep:#7fb89a;
  --wine:#b46b75;
  --wine-deep:#3a2a2a;
  --champagne:#fff6dd;
  --champagne-deep:#6f7048;
}
*{box-sizing:border-box;margin:0;padding:0}
html,body{width:1200px;height:5190px;overflow:hidden}
body{background:var(--ink);font-family:"Crimson Text",Georgia,serif;color:var(--white)}

.hero{position:relative;height:675px;overflow:hidden}
.hero-photo{position:absolute;inset:0;background:
  radial-gradient(ellipse at 85% 80%,rgba(120,80,50,.55),transparent 45%),
  radial-gradient(ellipse at 12% 40%,rgba(110,75,50,.45),transparent 40%),
  linear-gradient(100deg,#2b1c14 0%,#3d2a1e 25%,#1c130e 50%,#2f2119 75%,#3a281b 100%)}
.hero-shade{position:absolute;inset:0;background:rgba(0,0,0,.3)}
.brand{position:absolute;left:34px;top:28px;display:flex;align-items:center;gap:7px;
  font-size:12px;letter-spacing:1px;color:var(--white)}
.brand-mark{width:10px;height:10px;background:var(--gold)}
.nav{position:absolute;top:23px;left:0;width:1200px;display:flex;justify-content:center;gap:46px}
.nav a{display:block;border:1px solid rgba(255,255,255,.75);color:var(--white);text-decoration:none;
  font-size:11px;letter-spacing:.5px;padding:6px 16px;line-height:14px}
.hero-copy{position:absolute;top:228px;left:0;width:1200px;text-align:center}
.hero-title{font-size:74px;font-weight:600;line-height:1;letter-spacing:1px}
.hero-rule{width:392px;height:1px;background:rgba(255,255,255,.6);margin:28px auto 24px}
.hero-text{font-size:19px;line-height:25px;white-space:nowrap}

.products-head{height:155px;background:var(--band);text-align:center;padding-top:58px}
.products-head h2{font-size:29px;font-weight:400;letter-spacing:1px;line-height:1}
.gold-rule{width:50px;height:2px;background:var(--gold);margin:12px auto 0}

.product{display:flex;height:681px}
.product-name{width:600px;background:var(--ink);display:flex;flex-direction:column;align-items:center;justify-content:center;padding-bottom:20px}
.product-name h3{font-size:60px;font-weight:400;line-height:1}
.product-name .gold-rule{margin-top:22px}
.product-name.alt{background:var(--band-soft)}
.rose-rule{background:var(--rose)}
.product-photo{width:592px}
.whisky{background:radial-gradient(ellipse 34% 30% at 52% 46%,var(--whisky-deep),rgba(122,74,56,.35) 55%,transparent 80%),var(--whisky)}
.vodka{background:radial-gradient(ellipse 30% 38% at 50% 50%,var(--vodka-deep),rgba(143,183,216,.3) 55%,transparent 80%),var(--vodka)}
.rum{background:radial-gradient(ellipse 34% 30% at 56% 46%,var(--rum-deep),rgba(28,20,18,.35) 55%,transparent 80%),var(--rum)}
.gin{background:radial-gradient(ellipse 30% 36% at 52% 50%,var(--gin-deep),rgba(127,184,154,.3) 55%,transparent 80%),var(--gin)}
.wine{background:radial-gradient(ellipse 28% 38% at 54% 50%,var(--wine-deep),rgba(58,42,42,.35) 55%,transparent 80%),var(--wine)}
.champagne{background:radial-gradient(ellipse 28% 38% at 53% 50%,var(--champagne-deep),rgba(111,112,72,.3) 55%,transparent 80%),var(--champagne)}
.edge{width:8px;background:var(--band)}

.footer{height:274px;background:var(--band);position:relative}
.footer-brand{position:absolute;left:158px;top:90px}
.footer-name{font-size:28px;letter-spacing:2px;display:flex;align-items:center;gap:12px;line-height:1}
.footer-name .brand-mark{width:16px;height:16px}
.footer-tag{margin-top:30px;font-size:13px;line-height:17px}
.footer-divider{position:absolute;left:600px;top:44px;width:1px;height:172px;background:rgba(255,255,255,.7)}
.footer-contact{position:absolute;left:730px;top:60px;font-size:19px;line-height:22px}
.contact-row{display:flex;gap:12px;align-items:flex-start}
.contact-row + .contact-row{margin-top:22px}
.contact-row svg{flex:none;margin-top:3px}
</style>
</head>
<body>
<header class="hero">
  <div class="hero-photo" role="img" aria-label="Dim distillery interior with wooden door and oak barrel"></div>
  <div class="hero-shade"></div>
  <div class="brand"><span class="brand-mark"></span>MOSSGATE SPIRITWORKS</div>
  <nav class="nav">
    <a href="#">HOME</a><a href="#">WHOLESALE</a><a href="#">SERVICES</a><a href="#">CONTACT</a>
  </nav>
  <div class="hero-copy">
    <h1 class="hero-title">Wholesale</h1>
    <div class="hero-rule"></div>
    <p class="hero-text">We have exclusive access to spirits from world-class distilleries globally producing<br>award winning. We are able to supply large volumes of high-end spirit world-wide<br>if you wish to bottle in your own facility.</p>
  </div>
</header>

<section class="products-head">
  <h2>OUR PRODUCTS</h2>
  <div class="gold-rule"></div>
</section>

<section class="product">
  <div class="product-name"><h3>Whiskies</h3><div class="gold-rule"></div></div>
  <div class="product-photo whisky" role="img" aria-label="Whisky bottle with amber splash on peach background"></div>
  <div class="edge"></div>
</section>
<section class="product">
  <div class="product-name"><h3>Vodka</h3><div class="gold-rule"></div></div>
  <div class="product-photo vodka" role="img" aria-label="Premium vodka bottle with clear water splash on pale blue background"></div>
  <div class="edge"></div>
</section>
<section class="product">
  <div class="product-name"><h3>Rum</h3><div class="gold-rule"></div></div>
  <div class="product-photo rum" role="img" aria-label="Rum bottle with dark splash on brown background"></div>
  <div class="edge"></div>
</section>
<section class="product">
  <div class="product-name"><h3>Gins</h3><div class="gold-rule"></div></div>
  <div class="product-photo gin" role="img" aria-label="Gin bottle with green-tinted splash on mint background"></div>
  <div class="edge"></div>
</section>
<section class="product">
  <div class="product-name"><h3>Wines</h3><div class="gold-rule rose-rule"></div></div>
  <div class="product-photo wine" role="img" aria-label="Wine bottle with red wine splash on rose background"></div>
  <div class="edge"></div>
</section>
<section class="product">
  <div class="product-name alt"><h3>Champagnes</h3><div class="gold-rule"></div></div>
  <div class="product-photo champagne" role="img" aria-label="Champagne bottle with golden splash on cream background"></div>
  <div class="edge"></div>
</section>

<footer class="footer">
  <div class="footer-brand">
    <div class="footer-name"><span class="brand-mark"></span>MOSSGATE SPIRITWORKS</div>
    <p class="footer-tag">Turn your next drink idea into a reality and<br>share your product with the world.</p>
  </div>
  <div class="footer-divider"></div>
  <div class="footer-contact">
    <div class="contact-row">
      <svg width="14" height="14" viewBox="0 0 24 24" fill="var(--gold)"><path d="M6.6 10.8a15.1 15.1 0 0 0 6.6 6.6l2.2-2.2c.3-.3.7-.4 1-.2 1.1.4 2.3.6 3.6.6.6 0 1 .4 1 1V20c0 .6-.4 1-1 1A17 17 0 0 1 3 4c0-.6.4-1 1-1h3.5c.6 0 1 .4 1 1 0 1.3.2 2.5.6 3.6.1.3 0 .7-.2 1z"/></svg>
      <span>+31645170283</span>
    </div>
    <div class="contact-row">
      <svg width="14" height="16" viewBox="0 0 24 28" fill="none" stroke="var(--gold)" stroke-width="2.4"><path d="M12 26s-9-9-9-15a9 9 0 0 1 18 0c0 6-9 15-9 15z"/><circle cx="12" cy="11" r="3"/></svg>
      <span>Mossgate Spiritworks Building 12,<br>Harbourside Park, 3e<br>Lindelaan,<br>Noordwijk, 2201XK</span>
    </div>
  </div>
</footer>
</body>
</html>
```